beauty salon

providing waxing services from a home base this must include which I will provide a price list and an address

Industry/Entity Type

Beauty Salon

Font styles to use
Script

Colors

Designer to choose colors to be used in the design.

```html
<!DOCTYPE html>
<html lang="en">
<head>
<meta charset="utf-8">
<title>Rosalind's Garden Salon – Price List</title>
<link rel="stylesheet" href="https://fonts.googleapis.com/css2?family=Kaushan+Script&family=Dancing+Script:wght@500;700&family=Cabin:wght@500&display=swap">
<style>
  :root {
    --orange-light: #ffc83a;
    --orange-mid: #ffb21c;
    --orange-deep: #f79a0c;
    --purple: #8a1fd0;
    --purple-deep: #3d18b8;
    --magenta: #c31fd6;
    --cream: #fffbe8;
    --skin-light: #f7e3d8;
    --skin-mid: #e9c4b1;
    --hair: #6b4a3a;
  }
  * { margin: 0; padding: 0; box-sizing: border-box; }
  html, body { width: 1200px; height: 850px; overflow: hidden; background: #fff; }
  .flyer {
    position: relative; width: 1200px; height: 850px; overflow: hidden;
    background: radial-gradient(ellipse at 35% 35%, var(--orange-light) 0%, var(--orange-mid) 55%, var(--orange-deep) 100%);
  }
  .waves { position: absolute; left: 0; top: 560px; width: 935px; height: 290px; }
  .portrait {
    position: absolute; left: 933px; top: 0; width: 267px; height: 850px;
    background: linear-gradient(90deg, var(--skin-mid) 0%, var(--skin-light) 45%, #fbf1ec 80%, var(--hair) 100%);
  }
  .brand {
    position: absolute; left: 30px; top: 96px;
    display: flex; align-items: center; gap: 8px;
    font-family: "Cabin", sans-serif; font-weight: 500; font-size: 26px; color: var(--purple);
    white-space: nowrap;
  }
  .brand-dot { width: 14px; height: 14px; border-radius: 50%; background: var(--purple); }
  .script { font-family: "Kaushan Script", cursive; }
  .therapist {
    position: absolute; left: 5px; top: 150px; width: 410px; text-align: center;
    font-size: 28px; line-height: 40px; color: var(--purple-deep);
  }
  .contact { position: absolute; font-size: 29px; line-height: 39px; color: var(--purple-deep); white-space: nowrap; }
  .contact .label { position: absolute; color: var(--magenta); white-space: nowrap; font-size: 27px; }
  .mobile { left: 168px; top: 318px; }
  .mobile .label { left: -138px; }
  .address { left: 165px; top: 408px; }
  .address .label { left: -143px; }
  .hours { left: 165px; top: 506px; font-size: 30px; }
  .hours .label { left: -147px; font-size: 26px; }
  .price-list { position: absolute; left: 0; top: 0; }
  .price-title {
    position: absolute; left: 560px; top: 18px; width: 240px; text-align: center;
    font-family: "Dancing Script", cursive; font-weight: 700; font-size: 40px; color: var(--purple);
    white-space: nowrap;
  }
  .section-title {
    position: absolute; display: flex; align-items: center; gap: 10px;
    font-family: "Dancing Script", cursive; font-weight: 500; font-size: 29px; line-height: 36px;
    color: var(--purple); white-space: nowrap;
  }
  .section-title::before {
    content: ""; flex: none; width: 16px; height: 16px; border-radius: 50%; background: var(--magenta);
  }
  .prices {
    position: absolute; list-style: none;
    font-family: "Cabin", sans-serif; font-weight: 500; font-size: 19px; line-height: 30px; color: var(--cream);
    white-space: nowrap;
  }
  .prices li { position: relative; width: 190px; }
  .prices .amount { position: absolute; left: 137px; }
  .prices.right .amount { left: 144px; }
  .discount {
    position: absolute; left: 38px; top: 738px;
    font-size: 64px; color: var(--purple);
    text-shadow: 0 0 6px #fff, 0 0 12px rgba(255,255,255,.8);
    white-space: nowrap;
  }
</style>
</head>
<body>
<main class="flyer">
  <svg class="waves" viewBox="0 0 935 290" aria-hidden="true">
    <path d="M0 170 C200 110 420 80 600 150 S860 230 935 160 L935 290 L0 290 Z" fill="#ffd65a" opacity=".45"/>
    <path d="M0 200 C240 130 430 140 620 190 S850 220 935 120" fill="none" stroke="#fff3c0" stroke-width="3" opacity=".7"/>
    <path d="M0 225 C260 160 460 175 660 215 S860 210 935 150" fill="none" stroke="#fff3c0" stroke-width="2" opacity=".6"/>
  </svg>

  <div class="brand"><span class="brand-dot"></span>Rosalind's Garden Salon</div>

  <p class="therapist script">Beauty Therapist: Rosalind<br>Diploma of Beauty Therapy<br>at Marlow Academy</p>

  <p class="contact mobile script"><span class="label">Mobile:</span>0400 555 019</p>
  <p class="contact address script"><span class="label">Address:</span>12 Finch Lane<br>Eastbrook</p>
  <p class="contact hours script"><span class="label">Now Open:</span>Wednesday 10am – 4pm<br>Fridays 10am-7pm<br>Saturday 10am -4pm</p>

  <section class="price-list">
    <h1 class="price-title">Price List</h1>

    <h2 class="section-title" style="left:585px; top:82px;">Lady's Waxing</h2>
    <ul class="prices" style="left:498px; top:123px;">
      <li>Eyebrow<span class="amount">$8</span></li>
      <li>Upper lip<span class="amount">$8</span></li>
      <li>Chin<span class="amount">$8</span></li>
      <li>Face wax<span class="amount">$25</span></li>
      <li>Bikini line<span class="amount">$15</span></li>
      <li>G string<span class="amount">$20</span></li>
      <li>½ Brazilian<span class="amount">$30</span></li>
      <li>Full Brazilian<span class="amount">$40</span></li>
    </ul>
    <ul class="prices right" style="left:733px; top:120px;">
      <li>Half arm<span class="amount">$20</span></li>
      <li>Upper half arm<span class="amount">$20</span></li>
      <li>Full arm<span class="amount">$25</span></li>
      <li>Half leg<span class="amount">$15</span></li>
      <li>Upper leg<span class="amount">$20</span></li>
      <li>¾ Leg<span class="amount">$25</span></li>
      <li>Full leg<span class="amount">$35</span></li>
    </ul>

    <h2 class="section-title" style="left:585px; top:384px;">Eye Enhancement</h2>
    <ul class="prices" style="left:498px; top:428px;">
      <li>Eyebrow tint<span class="amount">$12</span></li>
    </ul>
    <ul class="prices right" style="left:733px; top:427px;">
      <li>Eyelash tint<span class="amount">$15</span></li>
    </ul>

    <h2 class="section-title" style="left:585px; top:479px;">Men's Waxing</h2>
    <ul class="prices" style="left:498px; top:530px;">
      <li>Eyebrow<span class="amount">$10</span></li>
      <li>Half arm<span class="amount">$20</span></li>
      <li>Upper half arm<span class="amount">$25</span></li>
      <li>Full arm<span class="amount">$30</span></li>
    </ul>
    <ul class="prices right" style="left:733px; top:528px;">
      <li>Half leg<span class="amount">$25</span></li>
      <li>Full leg<span class="amount">$45</span></li>
      <li>Chest wax<span class="amount">$40</span></li>
      <li>Back wax<span class="amount">$35</span></li>
    </ul>
  </section>

  <p class="discount script">-10% discount on first treatment.</p>

  <div class="portrait" role="img" aria-label="Beauty photograph of a woman with clear skin, hand resting on her cheek"></div>
</main>
</body>
</html>
```